Trade show Banner 10 x 10. Wood truck flooring

I would like to have a trade show banner created that will eventually be 10x 10. I am attaching a brochure and I would like most of the information that is on the brochure on the banner. no need for the address or phone. I would like the background to be in black
I will attach the brochure; however, will need to use dropbox or some other means to provide pictures. I have about 6 different pictures and not sure which ones to use but I would like different examples.

something modern, yet clean.
Updates

Project Deadline Extended Reason: I need a few days to meet with my team and then have a few days to make changes if needed. My team does not work on the weekend and we will meet this monday. Added Friday, December 11, 2015

Target Market(s)

Companies that either make truck flooring or repair it. We sell,the wood that is used on the truck bed

Industry/Entity Type

Flooring

Font styles to use
Serif

Requirements
Must have
• clean and modern. logo on www.brennolbedplank.com
Nice to have
• Clean and modern
Should not have
• Clutter

```html
<!DOCTYPE html>
<html lang="en">
<head>
<meta charset="utf-8">
<title>Brennol International – Truck &amp; Trailer Flooring Banner</title>
<link href="https://fonts.googleapis.com/css2?family=Ubuntu:wght@400;500;700&display=swap" rel="stylesheet">
<style>
  :root {
    --black: #0d0d0d;
    --white: #ffffff;
    --brown-dark: #5a3415;
    --brown: #8a5528;
    --brown-light: #a56c3a;
    --green: #7cc242;
    --green-dark: #4f8a22;
    --green-tile: #6fae3a;
    --logo-green: #5aa62c;
    --gold: #e3a52a;
    --gold-dark: #b97d18;
    --wood: #c9ad8a;
    --wood-dark: #8d7558;
  }
  * { margin: 0; padding: 0; box-sizing: border-box; }
  html, body { width: 1200px; height: 1108px; overflow: hidden; }
  body { background: var(--black); font-family: "Ubuntu", sans-serif; color: var(--white); }
  .banner { position: relative; width: 1200px; height: 1108px; background: var(--black); overflow: hidden; }

  .header { position: absolute; left: 0; top: 0; width: 1200px; height: 200px;
    background: linear-gradient(90deg, var(--brown-dark), var(--brown) 55%, var(--brown-light) 80%, var(--brown-dark)); }
  .header-white { position: absolute; left: 0; top: 0; width: 1200px; height: 200px; }
  .brand { position: absolute; left: 60px; top: 48px; display: flex; align-items: center; gap: 14px; }
  .brand-mark { width: 22px; height: 22px; background: var(--logo-green); }
  .brand-name { font-size: 54px; font-weight: 500; color: var(--logo-green); line-height: 1; }
  .brand-sub { position: absolute; left: 60px; top: 118px; font-size: 17px; letter-spacing: 5px; color: var(--logo-green); font-weight: 500; }
  .tagline { position: absolute; left: 512px; top: 34px; }
  .tagline-small { font-size: 44px; font-weight: 500; line-height: 1.2; }
  .tagline-large { font-size: 55px; font-weight: 500; line-height: 1.2; margin-left: 28px; }
  .stripe { position: absolute; left: 0; width: 1200px; height: 7px; background: var(--green); }
  .stripe.top { top: 200px; }
  .stripe.bottom { top: 1084px; }

  .hero-photo { position: absolute; left: 0; top: 207px; width: 1200px; height: 366px;
    background: linear-gradient(160deg, #2a2a2a 0%, var(--wood-dark) 18%, var(--wood) 45%, #b99c78 70%, #3a3a3a 100%); }

  .seal { position: absolute; left: 952px; top: 446px; width: 186px; height: 186px; border-radius: 50%;
    background: radial-gradient(circle, var(--gold) 60%, var(--gold-dark)); }

  .offer { position: absolute; left: 61px; top: 598px; }
  .offer-title { font-size: 48px; font-weight: 500; line-height: 1.15; }
  .offer-sub { font-size: 29px; font-weight: 500; line-height: 1.2; margin-top: 2px; }

  .products { position: absolute; left: 60px; top: 707px; width: 1090px; list-style: none;
    display: grid; grid-template-columns: repeat(3, 1fr); column-gap: 44px; row-gap: 28px; }
  .product-tile { position: relative; height: 68px; display: flex; align-items: center; justify-content: center;
    background: linear-gradient(180deg, #86c450, var(--green-tile) 50%, var(--green-dark));
    font-size: 36px; font-weight: 500; color: var(--white); text-shadow: 0 2px 2px rgba(0,0,0,0.35); }
  .product-tile::before, .product-tile::after { content: ""; position: absolute; top: 9px; width: 6px; height: 6px; border-radius: 50%;
    background: #cfe8b8; box-shadow: 0 44px 0 #cfe8b8; }
  .product-tile::before { left: 10px; }
  .product-tile::after { right: 10px; }

  .gallery { position: absolute; left: 0; top: 891px; width: 1200px; height: 180px; display: grid;
    grid-template-columns: 315px 384px 1fr; column-gap: 19px; }
  .gallery-photo { height: 100%; }
  .gallery-photo.cable { background: linear-gradient(180deg, #8aa0b8, #6b6e5c 55%, #4a4a48); }
  .gallery-photo.spools { background: linear-gradient(180deg, #c8c8c2, #b08a5e 50%, #3c3c3c); }
  .gallery-photo.mountain { background: linear-gradient(180deg, #a9c4e2, #d4dbe0 25%, #3e5a38 55%, #6a6e70); }
</style>
</head>
<body>
<main class="banner">
  <header class="header">
    <svg class="header-white" viewBox="0 0 1200 200" aria-hidden="true">
      <polygon points="0,0 370,0 580,200 0,200" fill="#ffffff"/>
    </svg>
    <div class="brand">
      <span class="brand-mark"></span>
      <span class="brand-name">Brennol</span>
    </div>
    <div class="brand-sub">International, Inc.</div>
    <div class="tagline">
      <div class="tagline-small">Your Natural Choice for...</div>
      <div class="tagline-large">Truck &amp; Trailer Flooring</div>
    </div>
  </header>
  <div class="stripe top"></div>

  <div class="hero-photo" role="img" aria-label="Photo of a flatbed trailer deck laid with wooden planks"></div>

  <div class="seal" role="img" aria-label="Buy direct from importer seal"></div>

  <section class="offer">
    <h1 class="offer-title">WE ARE SELLING APITONG - KERUING</h1>
    <p class="offer-sub">Full line of inventory stocked year round, Delevered across the U.S.A and Canada</p>
  </section>

  <ul class="products">
    <li class="product-tile">S4S</li>
    <li class="product-tile">T&amp;G</li>
    <li class="product-tile">Shiplap</li>
    <li class="product-tile">Bullnose</li>
    <li class="product-tile">Tie Down Slats</li>
    <li class="product-tile">Rough Lumber</li>
  </ul>

  <section class="gallery">
    <div class="gallery-photo cable" role="img" aria-label="Photo of a flatbed truck hauling cable coils on a highway"></div>
    <div class="gallery-photo spools" role="img" aria-label="Photo of large wooden cable spools chained to a trailer deck"></div>
    <div class="gallery-photo mountain" role="img" aria-label="Photo of a semi truck with flatbed trailer on a mountain road"></div>
  </section>
  <div class="stripe bottom"></div>
</main>
</body>
</html>
```